Stationery Required - Own Logo provided

Hi,

We are a retail company called 'Copperfinch Trading Limited' based in the UK and would like some corporate stationery designed.

We have provided our Logo which we would like to use (Its attached to this brief)...

The designs must be orginal, professional, stylish and interesting!

Target Market(s)

We will use this stationery to communicate with our wholesale suppliers and employees, so it must have a 'professional' feel about it.

Industry/Entity Type

It Company

Requirements
Must have
• Must be professional, corporate, stylish and not to 'fussy'. we require ... Business card design, a4 letter, compliment slip. All designs must be supplied in a format where the text (address/telephone numbers etc..) can be edited, as we have alot of staff and operate out of several different premises.
Nice to have
• I would like a windows backround picture file supplied as well so we can integrate that onto our computer systems.

```html
<!DOCTYPE html>
<html lang="en">
<head>
<meta charset="utf-8">
<title>Copperfinch Trading Limited – Letterhead</title>
<link rel="stylesheet" href="https://fonts.googleapis.com/css2?family=Nunito+Sans:wght@400;600&display=swap">
<style>
  :root {
    --backdrop: #f1f1f1;
    --paper: #ffffff;
    --green-dark: #2f6b0d;
    --green-bright: #8cf01c;
    --paper-edge: #dcdcdc;
  }
  * { box-sizing: border-box; margin: 0; padding: 0; }
  html, body {
    width: 1200px;
    height: 900px;
    overflow: hidden;
    background: var(--backdrop);
  }
  .canvas {
    position: relative;
    width: 1200px;
    height: 900px;
  }
  .letterhead {
    position: absolute;
    left: 246px;
    top: 30px;
    width: 584px;
    height: 830px;
    background: var(--paper);
    border: 1px solid var(--paper-edge);
  }
  .edge-band {
    position: absolute;
    top: 0;
    left: 0;
    height: 100%;
  }
  .edge-band--dark {
    width: 28px;
    background: var(--green-dark);
  }
  .edge-band--bright {
    left: 28px;
    width: 18px;
    background: var(--green-bright);
  }
  .brand {
    position: absolute;
    left: 58px;
    top: 34px;
    display: flex;
    align-items: center;
    gap: 12px;
  }
  .brand__square {
    width: 34px;
    height: 34px;
    background: var(--green-bright);
    flex: none;
  }
  .brand__name {
    font-family: "Nunito Sans", Arial, sans-serif;
    font-weight: 600;
    font-size: 32px;
    line-height: 1;
    color: var(--green-dark);
    letter-spacing: 0.2px;
  }
  .contact {
    position: absolute;
    left: 58px;
    bottom: 20px;
    font-family: "Nunito Sans", Arial, sans-serif;
    font-weight: 400;
    font-size: 13px;
    line-height: 16px;
    color: var(--green-bright);
    font-style: normal;
  }
</style>
</head>
<body>
  <main class="canvas">
    <section class="letterhead" aria-label="Copperfinch Trading Limited letterhead">
      <div class="edge-band edge-band--dark"></div>
      <div class="edge-band edge-band--bright"></div>

      <header class="brand">
        <span class="brand__square" aria-hidden="true"></span>
        <span class="brand__name">Copperfinch Trading Limited</span>
      </header>

      <address class="contact">
        <div class="contact__phone">0790-555-0142</div>
        <div class="contact__email">hello@copperfinch.co.uk</div>
        <div class="contact__street">18 Mill Lane Road</div>
        <div class="contact__town">Larkhill, County Down BT30 4QP</div>
      </address>
    </section>
  </main>
</body>
</html>
```